Finch Haulage Ltd

We need an A5 size (UK size) flyer to advertise our new business which is called Finch Haulage.
Domestic and Commercial Waste Clearance Services.
Please have the question in bold "Do you have a pile of junk you need to dispose of?"
We collect all kinds of junk or rubbish from homes and businesses across Kent, Sussex and South London.
No fuss, no mess!
A low cost, hassle free alternative to skip hire.
Licensed by the Landcare Board and fully insured (this can be in small print at the bottom).
Please put the Recycle symbol somewhere.
Our tagline on our vehicle is "We Clear More, For Less!"
We'd like the flyer to be bold and eye-catching (to catch the eye of the homeowner or business owner while it's sitting on their doormat).
We need our telephone, website and email to be prominent. Maybe saying "Call today for a free quote"
Tel. 01734 586019
Email: info@finchhaulage.example.co.uk
www.finchhaulage.example.co.uk
Target Market(s)
Our market will be homes and small businesses around Kent, Sussex and South London.

```html
<!DOCTYPE html>
<html lang="en">
<head>
<meta charset="utf-8">
<title>Finch Haulage – Junk Clearance Flyer</title>
<link rel="stylesheet" href="https://fonts.googleapis.com/css2?family=Anton&family=Source+Sans+3:wght@600;700;800&display=swap">
<style>
  :root {
    --backdrop: #e4cfa8;
    --cream: #fcebc9;
    --orange: #f47b20;
    --beige: #e8dbc3;
    --ink: #111111;
    --plum-text: #2a0d3a;
    --plum: #2b0a38;
    --red: #ea1c24;
    --grey: #6f7073;
    --lime: #3cff1e;
    --recycle-green: #3fb324;
    --badge-green: #6dab3c;
  }
  * { margin: 0; padding: 0; box-sizing: border-box; }
  html, body { width: 821px; height: 1200px; overflow: hidden; }
  body { background: var(--backdrop); position: relative; font-family: "Source Sans 3", Arial, sans-serif; }

  .flyer {
    position: absolute; left: 40px; top: 83px; width: 735px; height: 1044px;
    background: var(--cream); overflow: hidden;
  }
  .headline-banner {
    position: absolute; left: 53px; top: 0; width: 629px; height: 131px;
    background: var(--orange);
    clip-path: polygon(0 0, 100% 0, 96% 100%, 4% 100%);
  }
  .headline {
    position: absolute; left: 0; right: 0; top: 10px;
    font-family: "Anton", "Arial Narrow", sans-serif; font-weight: 400;
    font-size: 50px; line-height: 54px; color: var(--ink);
    text-align: center; letter-spacing: 0.3px; white-space: nowrap;
  }
  .junk-photo {
    position: absolute; left: 0; top: 132px; width: 735px; height: 252px;
    background: linear-gradient(100deg, #b9bcc0 0%, #8a8d93 30%, #5c6a55 45%, #3a3f4d 60%, #b8a58a 80%, #8d7a63 100%);
  }
  .recycle-symbol {
    position: absolute; left: 280px; top: 142px; width: 180px; height: 170px;
  }
  .service-band {
    position: absolute; left: 0; top: 384px; width: 735px; height: 140px;
    background: var(--orange);
    font-weight: 600; font-size: 36px; line-height: 40px; color: var(--ink);
    text-align: center; padding-top: 10px; white-space: nowrap;
  }
  .pitch-area {
    position: absolute; left: 0; top: 524px; width: 735px; height: 520px;
    background: var(--beige);
  }
  .pitch {
    position: absolute; left: 0; right: 0; top: 536px;
    font-family: "Anton", "Arial Narrow", sans-serif;
    font-size: 47px; line-height: 55px; color: var(--plum-text);
    text-align: center; padding-right: 70px; white-space: nowrap;
  }
  .call-prompt {
    position: absolute; left: 0; right: 0; top: 710px; padding-right: 60px;
    font-weight: 700; font-size: 32px; letter-spacing: -0.6px; color: var(--ink);
    text-align: center;
  }
  .phone {
    position: absolute; left: 120px; top: 750px;
    display: flex; align-items: center; gap: 4px; white-space: nowrap;
    font-weight: 700; font-size: 58px; letter-spacing: 2px; color: var(--red);
  }
  .phone svg { width: 50px; height: 50px; }
  .contact-panel { position: absolute; left: 0; top: 780px; width: 735px; height: 215px; }
  .web-contacts {
    position: absolute; left: 26px; top: 912px;
    transform: rotate(-8deg); transform-origin: left top;
    font-weight: 700; font-size: 21px; line-height: 26px; color: var(--orange);
    white-space: nowrap;
  }
  .web-contacts .email { display: flex; align-items: center; gap: 4px; }
  .web-contacts svg { width: 26px; height: 18px; }
  .brand-name {
    position: absolute; left: 400px; top: 872px; width: 310px;
    display: flex; align-items: center; gap: 10px; justify-content: center;
    font-weight: 800; font-size: 38px; color: var(--grey); white-space: nowrap;
  }
  .brand-name .dot { width: 20px; height: 20px; border-radius: 50%; background: var(--grey); flex: none; }
  .tagline {
    position: absolute; right: 26px; top: 952px;
    font-weight: 800; font-size: 26px; color: var(--lime); white-space: nowrap;
  }
  .licence-band {
    position: absolute; left: 0; top: 995px; width: 735px; height: 49px;
    background: var(--orange);
  }
  .licence-badge {
    position: absolute; left: 139px; top: 976px; width: 64px; height: 64px;
    border-radius: 50%; background: var(--badge-green); border: 4px solid #ffffff;
  }
  .licence-text {
    position: absolute; left: 212px; top: 1002px;
    font-weight: 700; font-size: 16px; line-height: 18px; color: var(--ink); white-space: nowrap;
  }
  .licence-text .insured { display: block; padding-left: 24px; letter-spacing: 0.6px; font-size: 15px; }
</style>
</head>
<body>
  <main class="flyer">
    <div class="headline-banner"></div>
    <h1 class="headline">Do you have a pile of junk<br>you need to dispose of?</h1>

    <div class="junk-photo" role="img" aria-label="Photograph of piled-up old computers, bin bags and cardboard boxes"></div>

    <svg class="recycle-symbol" viewBox="-100 -100 200 200" role="img" aria-label="Recycling symbol">
      <g id="recycle-arrow" fill="var(--recycle-green)" stroke="#1f7a12" stroke-width="2">
        <path d="M10.4 -59.1 A60 60 0 0 1 59.1 10.4" fill="none" stroke="var(--recycle-green)" stroke-width="20"/>
        <polygon points="55.3,34 82,14 36,6"/>
      </g>
      <use href="#recycle-arrow" transform="rotate(120)"/>
      <use href="#recycle-arrow" transform="rotate(240)"/>
    </svg>

    <p class="service-band">We collect all kinds of junk or rubbish<br>from homes and businesses across<br>Kent, Sussex and South London.</p>

    <div class="pitch-area"></div>
    <p class="pitch">No fuss, no mess!<br>A low cost, hassle free<br>alternative to skip hire.</p>

    <p class="call-prompt">Call today for a free quote</p>
    <p class="phone">
      <svg viewBox="0 0 50 50" aria-hidden="true">
        <circle cx="25" cy="25" r="21" fill="none" stroke="var(--red)" stroke-width="3"/>
        <path d="M18 13c-3 2-4 6-2 11s6 10 11 13c4 2 7 1 9-2l-5-5-3 2c-3-1-6-4-7-7l2-3z" fill="none" stroke="var(--red)" stroke-width="2.5" stroke-linejoin="round"/>
      </svg>
      01734 586019
    </p>

    <svg class="contact-panel" viewBox="0 0 735 215" preserveAspectRatio="none" aria-hidden="true">
      <polygon points="0,108 735,0 735,215 0,215" fill="var(--plum)"/>
    </svg>

    <div class="web-contacts">
      <div class="email">
        <svg viewBox="0 0 28 20" aria-hidden="true"><rect x="1.5" y="1.5" width="25" height="17" fill="none" stroke="var(--orange)" stroke-width="2.5"/><path d="M2 2l12 10L26 2" fill="none" stroke="var(--orange)" stroke-width="2.5"/></svg>
        info@finchhaulage.example.co.uk
      </div>
      <div>www.finchhaulage.example.co.uk</div>
    </div>

    <div class="brand-name"><span class="dot"></span>Finch Haulage</div>
    <p class="tagline">We Clear More, For Less!</p>

    <div class="licence-band"></div>
    <div class="licence-badge"></div>
    <p class="licence-text">Licensed by the Landcare Board<span class="insured">FULLY INSURED</span></p>
  </main>
</body>
</html>
```